Web Design Project

Brightwater Digital owns and operates a large number of editorial websites. These websites provides mostly consumers in the financial services space with information and price comparisons for a particular service.

Brightwater Digital, as the holding company for each of these sites, currently has no website. We need to build a website targeted towards potential partners for our websites. The idea being that when we start a conversation with a partner, they can view our site and obtain some basic information about who we are.

The structure of the site is to be very simple, containing only a brief description about who we are, our contact details and a list of some of our websites:
• CoverQuest.net.au
• AutoPolicyMatcher.com.au
• NestPolicyMatcher.com.au
• WellPolicyMatcher.com.au
• CoverQuestMatcher.com.au
• TripPolicyMatcher.com.au
• CritterPolicyMatcher.com.au
• CashAdvanceMatcher.com.au
• MobileCoolingUnit.com.au
• FixedSaverYields.com.au
• ThriftyHabits.com.au
• PurseGran.com.au
• TameThePlastic.com.au
• PurseMinder.com.au
• ThirdPartyClaimsCoverOzland.com.au
• Trade-Protect.com.au
• AutoPolicyProviders.com.au
• WellPolicyProviders.com.au
• NestPolicyOzland.com
• CoverQuestOzland.com
• WageShieldPolicyOzland.com
• WellPolicyOzland.com
• CritterPolicyOzland.com
• CashAdvancesOzland.com
• PlasticPaysOzland.com
• NestLendersOzland.com
• NestEggFunds.net.au

The design of the site should say 'Internet company', 'professional', 'fresh thinking'. The design should not look like a corporate site that you would see from any corporate services business with images of people in suits. We are ultimately an Internet business and there should be a unique feel to the site.

We are open to a suggestion of a colour pallet as the holding company does not have an established logo.

Some sites that we like are:

http://www.prismwork-studio.co.uk/#home
http://sample00.layoutvault.example/wt_48248/index.html
http://sample00.layoutvault.example/wordpress_46388/
http://mindvolt.example/
http://www.tandora.us/
http://www.kelvorabintu.example/
http://www.slickfrontpages.example/Corporate/design-ideas-detail.html?id=7916
http://trebla.example/
http://orvantek.example/

Reason: Hi all, Apologies, but I need to extend the timeline. One of our key stakeholders is away for the next week. There are a few good designs that we have received to date and there are some tweaks that we would like to see before making a final decision. Thank you to everyone that has submitted designs - Have a great new year. Derek

Reason: Sorry to have to delay the deadline on this, but we did not find anything in the designs really resonated with us. We will have a further think about the existing designs that have been submitted and how we can provide more specific feedback to the designers to make some modifications to the designs.

Target Market(s)

We are targeting insurance companies / brokers that we are talking to. The idea is that we show a professional face to them.

Industry/Entity Type

Financial

Requirements
Must have
• Home Page (possibly integrated with About us details)
Contact Us
Our Sites

```html
<!DOCTYPE html>
<html lang="en">
<head>
<meta charset="utf-8">
<title>Brightwater Digital</title>
<link rel="stylesheet" href="https://fonts.googleapis.com/css2?family=Arimo:wght@400;700&family=Exo+2:ital,wght@1,800;1,900&family=Parisienne&display=swap">
<style>
  :root {
    --header-bg: #d0c9b3;
    --band-bg: #efece0;
    --lower-bg: #c5bdaa;
    --card-bg: #ecebdf;
    --nav-active: #bdb6a2;
    --ink: #111;
    --muted: #555;
    --footer-ink: #7a766c;
    --accent-red: #e01010;
    --coral-a: #ff7f66;
    --coral-b: #ffa477;
    --green-a: #c4d83a;
    --green-b: #e2ea45;
    --yellow-a: #fdb522;
    --yellow-b: #fcdb52;
    --red-a: #ff6f66;
    --red-b: #ffa577;
    --blue-a: #5cc4f8;
    --blue-b: #72e2fb;
    --quote-green: #7aa61c;
    --rss: #f0641e;
  }
  * { box-sizing: border-box; margin: 0; padding: 0; }
  html, body { width: 1200px; height: 962px; overflow: hidden; }
  body { position: relative; font-family: "Arimo", Arial, sans-serif; background: var(--lower-bg); color: var(--ink); }
  .site-header { position: absolute; left: 0; top: 0; width: 1200px; height: 113px; background: var(--header-bg); }
  .brand { position: absolute; left: 130px; top: 38px; display: flex; align-items: center; gap: 10px; font-size: 31px; font-weight: 700; color: #1a1a1a; letter-spacing: -0.5px; }
  .brand-dot { width: 14px; height: 14px; border-radius: 50%; background: #5aa82a; }
  .main-nav { position: absolute; top: 33px; left: 640px; height: 50px; }
  .main-nav a { position: absolute; top: 0; height: 50px; line-height: 50px; font-size: 14px; color: var(--ink); text-decoration: none; white-space: nowrap; }
  .main-nav .is-active { left: 0; width: 95px; text-align: center; background: var(--nav-active); border-radius: 6px; }
  .feature-band { position: absolute; left: 0; top: 113px; width: 1200px; height: 514px; background: var(--band-bg); }
  .hero { position: absolute; left: 130px; top: 30px; width: 940px; height: 382px; border-radius: 14px; overflow: hidden; background: linear-gradient(110deg, #a8e4f6 0%, #c3ecf7 45%, #b0e6f8 100%); }
  .hero-photo { position: absolute; right: 0; top: 0; width: 540px; height: 382px; background: radial-gradient(ellipse at 62% 55%, #e9c9b4 0%, #e6c6b8 30%, #cfdce6 60%, rgba(178,230,248,0) 80%); }
  .hero-title { position: absolute; left: 59px; top: 113px; width: 470px; font-family: "Exo 2", sans-serif; font-style: italic; font-weight: 900; font-size: 34px; line-height: 29px; color: #fff; }
  .join-button { position: absolute; left: 59px; top: 217px; width: 142px; height: 53px; border-radius: 14px; background: linear-gradient(90deg, var(--coral-a), var(--coral-b)); color: #fff; font-family: "Exo 2", sans-serif; font-style: italic; font-weight: 800; font-size: 19px; line-height: 53px; text-align: center; }
  .categories { position: absolute; left: 130px; top: 433px; width: 940px; height: 61px; }
  .category { position: absolute; top: 0; width: 230px; height: 61px; border-radius: 10px; color: #fff; }
  .category-name { position: absolute; left: 30px; top: 15px; font-family: "Exo 2", sans-serif; font-style: italic; font-weight: 900; font-size: 23px; }
  .category-link { position: absolute; left: 131px; top: 22px; font-family: Georgia, serif; font-size: 13px; }
  .category svg { position: absolute; left: 197px; top: 25px; }
  .cat-health { left: 0; background: linear-gradient(90deg, var(--green-a), var(--green-b)); }
  .cat-life { left: 236px; background: linear-gradient(90deg, var(--yellow-a), var(--yellow-b)); }
  .cat-auto { left: 473px; background: linear-gradient(90deg, var(--red-a), var(--red-b)); }
  .cat-home { left: 709px; background: linear-gradient(90deg, var(--blue-a), var(--blue-b)); }
  .card { position: absolute; background: var(--card-bg); border-radius: 5px; box-shadow: 3px 4px 6px rgba(90, 80, 60, 0.35); }
  .card-about { left: 130px; top: 655px; width: 297px; height: 249px; }
  .card-sites { left: 452px; top: 655px; width: 298px; height: 249px; }
  .card-contact { left: 773px; top: 657px; width: 297px; height: 111px; }
  .card-news { left: 773px; top: 790px; width: 297px; height: 111px; }
  .card-icon { position: absolute; top: 29px; width: 14px; height: 15px; border: 1px solid #aaa; background: #fff; }
  .card-icon::after { content: ""; position: absolute; right: -3px; bottom: -2px; width: 8px; height: 8px; background: #f08a1c; border-radius: 2px; }
  .card-title { position: absolute; top: 27px; font-size: 16px; font-weight: 400; color: var(--ink); }
  .card-subtitle { position: absolute; top: 44px; font-size: 12px; letter-spacing: 0.3px; color: var(--accent-red); }
  .card-about .card-icon { left: 29px; }
  .card-about .card-title, .card-about .card-subtitle { left: 53px; }
  .card-body { position: absolute; left: 29px; top: 67px; width: 262px; font-size: 12px; line-height: 19.2px; color: var(--muted); text-align: justify; letter-spacing: 0.2px; }
  .read-more { position: absolute; left: 30px; top: 187px; width: 91px; height: 46px; border-radius: 12px; background: linear-gradient(90deg, var(--coral-a), var(--coral-b)); color: #fff; font-size: 13px; font-weight: 700; letter-spacing: 0.5px; line-height: 46px; text-align: center; }
  .card-sites .card-icon { left: 28px; }
  .card-sites .card-title { left: 52px; }
  .card-sites .card-subtitle { left: 53px; }
  .site-list { position: absolute; left: 30px; top: 78px; list-style: none; }
  .site-list li { position: relative; height: 29px; padding-left: 22px; font-size: 12px; letter-spacing: 0.4px; color: var(--muted); }
  .site-list li::before { content: ""; position: absolute; left: 2px; top: 3px; width: 6px; height: 6px; border-right: 2.5px solid #b06a10; border-top: 2.5px solid #b06a10; transform: rotate(45deg); }
  .contact-title { position: absolute; left: 25px; top: 6px; font-family: "Parisienne", cursive; font-weight: 400; font-size: 29px; color: var(--quote-green); white-space: nowrap; }
  .contact-label { position: absolute; left: 43px; top: 51px; font-size: 14px; color: #222; }
  .email-field { position: absolute; left: 41px; top: 71px; width: 117px; height: 33px; border: 1px solid #aaa; border-radius: 5px; background: #efefef; }
  .go-link { position: absolute; left: 167px; top: 70px; font-family: "Parisienne", cursive; font-size: 26px; color: var(--quote-green); text-decoration: underline; text-underline-offset: 3px; }
  .feed-icon { position: absolute; left: 6px; top: 15px; width: 81px; height: 81px; border-radius: 10px; background: linear-gradient(135deg, #f78a3a, var(--rss)); border: 2px solid #d8501a; }
  .feed-text { position: absolute; left: 92px; top: 43px; font-size: 15px; color: #777; letter-spacing: -0.2px; white-space: nowrap; }
  .site-footer { position: absolute; left: 149px; top: 931px; width: 897px; font-size: 12px; color: var(--footer-ink); display: flex; justify-content: space-between; }
</style>
</head>
<body>
  <header class="site-header">
    <div class="brand"><span>Brightwater Digital</span><span class="brand-dot"></span></div>
    <nav class="main-nav">
      <a class="is-active" href="#">Home</a>
      <a style="left:118px" href="#">About Us</a>
      <a style="left:217px" href="#">Contact Us</a>
      <a style="left:319px" href="#">Our Sites</a>
    </nav>
  </header>

  <section class="feature-band">
    <div class="hero">
      <div class="hero-photo" role="img" aria-label="Photo of a smiling mother carrying her young daughter on her back"></div>
      <h1 class="hero-title">Editorial sites that<br>connect partners with<br>informed buyers</h1>
      <div class="join-button">partner now!</div>
    </div>

    <div class="categories">
      <div class="category cat-health"><span class="category-name">Health</span><span class="category-link">click here</span><svg width="13" height="11" viewBox="0 0 13 11"><path d="M0 3.5h6V0l7 5.5-7 5.5V7.5H0z" fill="#fff"/></svg></div>
      <div class="category cat-life"><span class="category-name">Life</span><span class="category-link">click here</span><svg width="13" height="11" viewBox="0 0 13 11"><path d="M0 3.5h6V0l7 5.5-7 5.5V7.5H0z" fill="#fff"/></svg></div>
      <div class="category cat-auto"><span class="category-name">Auto</span><span class="category-link">click here</span><svg width="13" height="11" viewBox="0 0 13 11"><path d="M0 3.5h6V0l7 5.5-7 5.5V7.5H0z" fill="#fff"/></svg></div>
      <div class="category cat-home"><span class="category-name">Home</span><span class="category-link">click here</span><svg width="13" height="11" viewBox="0 0 13 11"><path d="M0 3.5h6V0l7 5.5-7 5.5V7.5H0z" fill="#fff"/></svg></div>
    </div>
  </section>

  <article class="card card-about">
    <span class="card-icon"></span>
    <h2 class="card-title">WHO WE ARE</h2>
    <p class="card-subtitle">an online publishing group</p>
    <p class="card-body">Brightwater Digital owns and runs a large network of editorial websites that give consumers in financial services clear information and price comparisons. We work with insurers and brokers to put their cover in front of ready buyers.</p>
    <div class="read-more">Read More</div>
  </article>

  <article class="card card-sites">
    <span class="card-icon"></span>
    <h2 class="card-title">OUR SITES</h2>
    <p class="card-subtitle">a few of our websites</p>
    <ul class="site-list">
      <li>CoverQuest.net.au</li>
      <li>AutoPolicyMatcher.com.au</li>
      <li>NestPolicyMatcher.com.au</li>
      <li>WellPolicyMatcher.com.au</li>
      <li>TripPolicyMatcher.com.au</li>
    </ul>
  </article>

  <aside class="card card-contact">
    <h2 class="contact-title">Talk To Us Now !</h2>
    <p class="contact-label">Enter your email address:</p>
    <div class="email-field"></div>
    <span class="go-link">Go!</span>
  </aside>

  <aside class="card card-news">
    <span class="feed-icon"></span>
    <p class="feed-text">Get the latest news &amp; updates</p>
  </aside>

  <footer class="site-footer">
    <span>Brightwater Digital (c) 2011 I Privacy policy</span>
    <span>Support&nbsp; I&nbsp; FAQs&nbsp; I&nbsp; Partners Area</span>
  </footer>
</body>
</html>
```